Book cover needed for a major new book on emotional resilience

The book will be titled: 'Stone to Stream: from habit bound to builders of renewal - The guide for growing steady teams and institutions'
My websites are http://www.pathmorrow.com and http://www.lumbrava.org and I am http://en.wikiverse-sample.org/wiki/Martin_Okonedo_(uncertainty_scholar) ad expert in developing emotional resilience. My previous book was The Murky Dividend.
The premise of the book is to introduce brand new material which is the first ever methodology and strategy on how to develop emotional resilience across entire populations like organisations and companies or moving people from fear about change to finding flow through resilience.
The final design should communicate the fact that this is a strategy and methodology. That it is about developing people and entire organisations to be more resilient and who are able to deal with change better.
Target Market(s)
Consultants, Organisational development consultants, Human Resource professionals.

```html
<!DOCTYPE html>
<html lang="en">
<head>
<meta charset="utf-8">
<title>Stone to Stream — Martin Okonedo</title>
<link href="https://fonts.googleapis.com/css2?family=Special+Elite&display=swap" rel="stylesheet">
<style>
  :root {
    --wall-light: #f3d6b4;
    --wall-mid: #d9a574;
    --wall-deep: #a9683b;
    --wall-shadow: #5a3218;
    --ink: #1d120b;
    --band: #0f0c0a;
    --band-text: #f1e6d6;
  }
  html, body {
    margin: 0;
    padding: 0;
    overflow: hidden;
  }
  body {
    width: 788px;
    height: 1200px;
    background: var(--wall-mid);
  }
  .cover {
    position: relative;
    width: 788px;
    height: 1200px;
    overflow: hidden;
    font-family: "Special Elite", "Courier New", monospace;
  }
  .cover-photo {
    position: absolute;
    inset: 0;
    background:
      radial-gradient(ellipse 60% 45% at 15% 95%, rgba(255, 240, 220, 0.85), rgba(255, 240, 220, 0) 70%),
      radial-gradient(ellipse 55% 70% at 78% 50%, rgba(90, 50, 24, 0.45), rgba(90, 50, 24, 0) 70%),
      linear-gradient(180deg, var(--wall-deep) 0%, var(--wall-mid) 30%, var(--wall-light) 65%, var(--wall-mid) 100%);
  }
  .author {
    position: absolute;
    left: 80px;
    top: 348px;
    margin: 0;
    font-size: 26px;
    font-weight: 400;
    line-height: 50px;
    letter-spacing: 5px;
    text-transform: uppercase;
    color: var(--ink);
  }
  .author span { display: block; }
  .title-band {
    position: absolute;
    left: 22px;
    top: 795px;
    width: 760px;
    height: 96px;
    background: var(--band);
    transform: rotate(-10.5deg);
    transform-origin: center;
    display: flex;
    align-items: center;
    justify-content: center;
  }
  .title {
    margin: 0;
    font-size: 58px;
    font-weight: 400;
    letter-spacing: 5px;
    text-transform: uppercase;
    color: var(--band-text);
    white-space: nowrap;
  }
  .subtitle {
    position: absolute;
    left: 0;
    right: 0;
    top: 1000px;
    margin: 0;
    text-align: center;
    font-size: 23px;
    font-weight: 400;
    line-height: 51px;
    letter-spacing: 4px;
    text-transform: uppercase;
    color: var(--ink);
  }
  .subtitle span { display: block; }
</style>
</head>
<body>
  <main class="cover">
    <div class="cover-photo" role="img" aria-label="Warm-toned photograph of a clothes rail against a plaster wall, with two empty wooden hangers and a short-sleeved shirt hanging on the right"></div>

    <p class="author">
      <span>Martin</span>
      <span>Okonedo</span>
    </p>

    <div class="title-band">
      <h1 class="title">Stone to Stream:</h1>
    </div>

    <p class="subtitle">
      <span>from habit bound to</span>
      <span>builders of renewal -</span>
      <span>the guide for growing</span>
      <span>steady teams and institutions</span>
    </p>
  </main>
</body>
</html>
```